Fun but corporate B2B Infographic

Infographic - for use on corporate [B2B] web site: https://www.vextrano.com/ +++++++++++++++Title of infographic: VEXTRANO, by the numbers- 7,322 Active users from - 61 different countries [1/3rd of the world] running- 14.8 million report calculations returning 6.5 Billion data points at an average of4.1 seconds to render a report - from request to presentation using reports developed with52 specialist Tablix functions surfaced in3 Brindle Suite Applications [Tablix – Slidemaker – Scriba] and across ALL web browsers All this wrapped in an All-In-One platform for Reporting, Business Intelligence, Budgeting and Forecasting.++++++++++++Will need 2x rounds of revisions - and preferably provide final artwork files for us to make tweaks to in the future.Use the images/logos and style guide attached.

Target Market(s)

CFOs and Financial controllers

Font styles to use
Sans Serif

Colors

Designer to choose colors to be used in the design.

Requirements
Must have
• graphics, fun icons matching the words - eg: we say "1/3rd of the world", so put an image of a globe or a map with the major countries identified/different colour.
• Although this is B2B, it also needs to be eye-catching and fun

```html
<!DOCTYPE html>
<html lang="en">
<head>
<meta charset="utf-8">
<title>VEXTRANO by the numbers</title>
<link rel="stylesheet" href="https://fonts.googleapis.com/css2?family=Encode+Sans+Semi+Condensed:wght@500;600;700&display=swap">
<style>
  :root {
    --navy: #0f2b60;
    --navy-soft: #1f3d74;
    --green: #7dc242;
    --white: #ffffff;
    --mist: #f2f3f5;
    --halo-light: #e3e7ee;
    --stage: #e6edf3;
  }
  * { box-sizing: border-box; margin: 0; padding: 0; }
  html, body { width: 1200px; height: 955px; overflow: hidden; }
  body {
    background: var(--stage);
    font-family: "Encode Sans Semi Condensed", "Arial Narrow", sans-serif;
    position: relative;
  }
  .infographic {
    --body-bg: var(--navy);
    --ink: var(--white);
    --halo: var(--navy-soft);
    --bar-bg: var(--mist);
    --bar-ink: var(--navy);
    position: absolute; top: 65px; width: 511px; height: 813px;
    background: var(--body-bg); overflow: hidden;
  }
  .infographic--dark { left: 70px; }
  .infographic--light {
    left: 619px;
    --body-bg: var(--white);
    --ink: var(--navy);
    --halo: var(--halo-light);
    --bar-bg: var(--navy);
    --bar-ink: var(--white);
  }
  .masthead, .tagline-bar {
    position: absolute; left: 0; width: 100%; background: var(--bar-bg); color: var(--bar-ink);
  }
  .masthead { top: 0; height: 76px; }
  .brand { position: absolute; left: 16px; top: 22px; display: flex; align-items: center; gap: 10px; }
  .brand__dot { width: 30px; height: 30px; border-radius: 50%; background: var(--green); }
  .brand__name { font-size: 34px; font-weight: 700; letter-spacing: 0.5px; line-height: 1; }
  .period { position: absolute; left: 340px; top: 11px; font-size: 24px; font-weight: 600; line-height: 28px; letter-spacing: -0.5px; }
  .tagline-bar { bottom: 0; height: 42px; display: flex; justify-content: center; align-items: center; gap: 10px; font-size: 21px; font-weight: 700; letter-spacing: 0.3px; }
  .tagline-bar .sep { width: 5px; height: 5px; border-radius: 50%; background: var(--green); }

  .t { position: absolute; line-height: 1; font-weight: 700; color: var(--ink); letter-spacing: -1px; white-space: nowrap; }
  .g { color: var(--green); }
  .halo { position: absolute; border-radius: 50%; background: var(--halo); }
  .art { position: absolute; }

  .stat-61 { left: 230px; top: 130px; font-size: 62px; color: var(--green); letter-spacing: -3px; }
  .stat-61-label { left: 292px; top: 136px; font-size: 24px; line-height: 19px; }
  .running { left: 39px; top: 178px; font-size: 27px; }
  .stat-148 { left: 102px; top: 201px; font-size: 46px; color: var(--green); letter-spacing: -2px; }
  .million { left: 192px; top: 214px; font-size: 28px; }
  .report { left: 154px; top: 246px; font-size: 35px; }
  .calculations { left: 146px; top: 282px; font-size: 28px; }
  .returning { left: 256px; top: 324px; font-size: 19px; color: var(--green); }
  .over { left: 232px; top: 370px; font-size: 27px; transform: rotate(-90deg); transform-origin: center; }
  .billion { left: 279px; top: 343px; font-size: 38px; color: var(--green); }
  .data-points { left: 279px; top: 378px; font-size: 34px; }
  .avg-label { left: 83px; top: 466px; font-size: 20px; }
  .seconds { left: 30px; top: 480px; font-size: 44px; color: var(--green); letter-spacing: -2.5px; }
  .developed { left: 203px; top: 542px; font-size: 28px; }
  .stat-52 { left: 341px; top: 545px; font-size: 42px; color: var(--green); }
  .with { left: 312px; top: 568px; font-size: 12px; letter-spacing: 0; }
  .unique { left: 313px; top: 577px; font-size: 22px; }
  .functions { left: 258px; top: 598px; font-size: 19px; }
  .suite-tile { position: absolute; top: 652px; width: 40px; height: 44px; border-radius: 4px; }
  .suite-line { left: 168px; top: 660px; font-size: 29px; color: var(--green); letter-spacing: -1px; }
  .browser-line { left: 34px; top: 706px; font-size: 32px; }
</style>
</head>
<body>

<article class="infographic infographic--dark">
  <header class="masthead">
    <div class="brand"><span class="brand__dot"></span><span class="brand__name">VEXTRANO</span></div>
    <p class="period">12 months<br>to Feb 2019</p>
  </header>

  <div class="halo" style="left:390px;top:107px;width:112px;height:112px"></div>
  <div class="art" role="img" aria-label="Globe on a stand with one third of the world highlighted" style="left:404px;top:116px;width:80px;height:80px;border-radius:50%;background:radial-gradient(circle at 35% 35%,#7dc242 0 25%,#a9c7de 26% 60%,#dfe9f1 100%)"></div>
  <p class="t stat-61">61</p>
  <p class="t stat-61-label">different<br>countries</p>

  <div class="halo" style="left:14px;top:223px;width:152px;height:152px"></div>
  <div class="art" role="img" aria-label="Report clipboard with charts and a calculator" style="left:20px;top:245px;width:120px;height:108px;border-radius:4px;background:linear-gradient(160deg,#ffffff 0 60%,#dfe5ec 61% 100%)"></div>
  <p class="t running">running</p>
  <p class="t stat-148">14.8</p>
  <p class="t million">million</p>
  <p class="t report">report</p>
  <p class="t calculations">calculations</p>

  <svg class="art" style="left:425px;top:280px" width="55" height="70" viewBox="0 0 55 70">
    <polyline points="8,62 15,38 36,32 46,8" fill="none" stroke="#7dc242" stroke-width="3"/>
    <circle cx="46" cy="8" r="4" fill="#7dc242"/><circle cx="36" cy="32" r="4" fill="#7dc242"/><circle cx="15" cy="38" r="4" fill="#7dc242"/>
  </svg>
  <p class="t returning">returning</p>
  <p class="t over">over</p>
  <p class="t billion">6.5 Billion</p>
  <p class="t data-points">data points</p>

  <svg class="art" style="left:228px;top:434px" width="76" height="80" viewBox="0 0 76 80">
    <rect x="32" y="0" width="12" height="8" fill="#fff"/>
    <rect x="8" y="6" width="7" height="10" fill="#fff" transform="rotate(-35 11 11)"/>
    <rect x="61" y="6" width="7" height="10" fill="#fff" transform="rotate(35 64 11)"/>
    <circle cx="38" cy="44" r="34" fill="#fff"/>
    <circle cx="38" cy="44" r="28" fill="#dfe5ec"/>
    <line x1="38" y1="44" x2="42" y2="20" stroke="#7dc242" stroke-width="3"/>
    <line x1="38" y1="44" x2="24" y2="58" stroke="#0f2b60" stroke-width="2"/>
  </svg>
  <p class="t avg-label">in of average</p>
  <p class="t seconds">4.1seconds</p>

  <div class="halo" style="left:384px;top:479px;width:106px;height:106px"></div>
  <div class="art" role="img" aria-label="Group of business people presenting a chart" style="left:396px;top:500px;width:96px;height:106px;border-radius:8px;background:linear-gradient(180deg,#3c5a8f,#7dc242)"></div>
  <p class="t developed">developed</p>
  <p class="t with">with</p>
  <p class="t stat-52">52</p>
  <p class="t unique">unique</p>
  <p class="t functions">Tablix functions</p>

  <span class="suite-tile" style="left:26px;background:#2d6fc0"></span>
  <span class="suite-tile" style="left:72px;background:#d9502f"></span>
  <span class="suite-tile" style="left:118px;background:#207245"></span>
  <p class="t suite-line">3 Brindle Suite add-ins</p>
  <p class="t browser-line">and access from <span class="g">ANY browser</span></p>

  <footer class="tagline-bar"><span>PREDICT</span><span class="sep"></span><span>SHAPE</span><span class="sep"></span><span>ACHIEVE</span></footer>
</article>

<article class="infographic infographic--light">
  <header class="masthead">
    <div class="brand"><span class="brand__dot"></span><span class="brand__name">VEXTRANO</span></div>
    <p class="period">12 months<br>to Feb 2019</p>
  </header>

  <div class="halo" style="left:390px;top:107px;width:112px;height:112px"></div>
  <div class="art" role="img" aria-label="Globe on a stand with one third of the world highlighted" style="left:404px;top:116px;width:80px;height:80px;border-radius:50%;background:radial-gradient(circle at 35% 35%,#7dc242 0 25%,#a9c7de 26% 60%,#0f2b60 100%)"></div>
  <p class="t stat-61">61</p>
  <p class="t stat-61-label">different<br>countries</p>

  <div class="halo" style="left:14px;top:223px;width:152px;height:152px"></div>
  <div class="art" role="img" aria-label="Report clipboard with charts and a calculator" style="left:20px;top:245px;width:120px;height:108px;border-radius:4px;background:linear-gradient(160deg,#ffffff 0 55%,#0f2b60 56% 100%);border:2px solid #0f2b60"></div>
  <p class="t running">running</p>
  <p class="t stat-148">14.8</p>
  <p class="t million">million</p>
  <p class="t report">report</p>
  <p class="t calculations">calculations</p>

  <svg class="art" style="left:425px;top:280px" width="55" height="70" viewBox="0 0 55 70">
    <polyline points="8,62 15,38 36,32 46,8" fill="none" stroke="#9aa5b5" stroke-width="3"/>
    <circle cx="46" cy="8" r="4" fill="#0f2b60"/><circle cx="36" cy="32" r="4" fill="#0f2b60"/><circle cx="15" cy="38" r="4" fill="#0f2b60"/>
  </svg>
  <p class="t returning">returning</p>
  <p class="t over">over</p>
  <p class="t billion">6.5 Billion</p>
  <p class="t data-points">data points</p>

  <svg class="art" style="left:228px;top:434px" width="76" height="80" viewBox="0 0 76 80">
    <rect x="32" y="0" width="12" height="8" fill="#0f2b60"/>
    <rect x="8" y="6" width="7" height="10" fill="#0f2b60" transform="rotate(-35 11 11)"/>
    <rect x="61" y="6" width="7" height="10" fill="#0f2b60" transform="rotate(35 64 11)"/>
    <circle cx="38" cy="44" r="34" fill="#0f2b60"/>
    <circle cx="38" cy="44" r="28" fill="#c9d8e6"/>
    <line x1="38" y1="44" x2="42" y2="20" stroke="#7dc242" stroke-width="3"/>
    <line x1="38" y1="44" x2="24" y2="58" stroke="#0f2b60" stroke-width="2"/>
  </svg>
  <p class="t avg-label">in of average</p>
  <p class="t seconds">4.1seconds</p>

  <div class="halo" style="left:384px;top:479px;width:106px;height:106px"></div>
  <div class="art" role="img" aria-label="Group of business people presenting a chart" style="left:396px;top:500px;width:96px;height:106px;border-radius:8px;background:linear-gradient(180deg,#0f2b60,#7dc242)"></div>
  <p class="t developed">developed</p>
  <p class="t with">with</p>
  <p class="t stat-52">52</p>
  <p class="t unique">unique</p>
  <p class="t functions">Tablix functions</p>

  <span class="suite-tile" style="left:26px;background:#2d6fc0"></span>
  <span class="suite-tile" style="left:72px;background:#207245"></span>
  <span class="suite-tile" style="left:118px;background:#d9502f"></span>
  <p class="t suite-line">3 Brindle Suite add-ins</p>
  <p class="t browser-line">and access from <span class="g">ANY browser</span></p>

  <footer class="tagline-bar"><span>PREDICT</span><span class="sep"></span><span>SHAPE</span><span class="sep"></span><span>ACHIEVE</span></footer>
</article>

</body>
</html>
```